Poster/Flyer design for a Church Youth Group Event

We need a flyer for Harvest Rally 2013. This event is being put on by 6 different churches. The event is for youth from 6th grade to 12th grade. The theme for this event is "Life By Faith" this is taken from Hebrews 11:1-39.
This flyer will be put up in both schools and the churches. It will also be included with the registration forms for the event.

Target Market(s)

Youth - Ages 11-18

Industry/Entity Type

Church

Requirements
Must have
• We would like the phrases "Life By Faith" and "Harvest Rally 2013" to be the focal point of the flyer. We would also like the the verse "Hebrews 11:1-39" on the flyer as well.
The date for the event - Feb. 6, 8-10
Cost - $25
There is some additional information that needs to be on the flyer as well:
Speaker - Dr. Morton Pasley
Worship Leader - Glen Abernathy
I've included pictures of the speaker and the worship leader. It would be nice to have the pics on the flyer, but it is not essential.

We need the names of the churches involved: FBC Marrow Creek, Venhurst Methodist, FBC Venhurst, Orrin Baptist, Hal Prewitt Ridge C of C, & Marrow Creek C of C. It doesn't really matter where or how these are on the design, as long as it is there

The flyer also needs to say "registration forms can be picked up in the office or from one of the churches"

I have included a picture of the t-shirt for the event. A similar design style would be great.

```html
<!DOCTYPE html>
<html lang="en">
<head>
<meta charset="utf-8">
<title>Harvest Rally 2013 – Life by Faith</title>
<link href="https://fonts.googleapis.com/css2?family=Yellowtail&family=Open+Sans:wght@600;700&family=Tinos:ital,wght@0,700;1,700&display=swap" rel="stylesheet">
<style>
  :root {
    --blue-deep: #1b2a9c;
    --blue-mid: #2a45d6;
    --blue-light: #3d5cf0;
    --cyan: #2bb3f0;
    --white: #ffffff;
    --band: rgba(190, 205, 255, 0.38);
    --shirt: #3a86d8;
    --shirt-dark: #1f5fae;
    --photo-a: #6a5a73;
    --photo-b: #7a6a58;
  }
  * { margin: 0; padding: 0; box-sizing: border-box; }
  html, body { width: 776px; height: 1200px; overflow: hidden; background: var(--blue-deep); }
  .flyer {
    position: relative; width: 776px; height: 1200px; overflow: hidden;
    background: radial-gradient(ellipse at 50% 40%, var(--blue-light) 0%, var(--blue-mid) 45%, var(--blue-deep) 100%);
    color: var(--white);
  }
  .script { font-family: "Yellowtail", cursive; }
  .sans { font-family: "Open Sans", sans-serif; font-weight: 700; }
  .serif { font-family: "Tinos", serif; font-weight: 700; }
  .abs { position: absolute; }

  .headline { top: 22px; left: 0; width: 100%; text-align: center; font-size: 46px; line-height: 1; }
  .invite { top: 104px; left: 0; width: 100%; text-align: center; font-size: 46px; line-height: 1; }
  .accent { color: var(--cyan); font-size: 1.15em; }
  .invite .plain { font-family: "Tinos", serif; font-weight: 700; font-size: 32px; }

  .photo { border: 5px solid var(--white); box-shadow: 0 4px 14px rgba(0,0,0,.45); }
  .photo-speaker { left: 20px; top: 164px; width: 268px; height: 236px; transform: rotate(-4deg);
    background: linear-gradient(160deg, #8b86c8 0%, #5c5aa0 55%, #2b2a40 100%); }
  .photo-worship { left: 34px; top: 466px; width: 310px; height: 252px; transform: rotate(6deg);
    background: linear-gradient(150deg, #b07a3a 0%, var(--photo-b) 45%, #3a2f2a 100%); }

  .event-name { top: 196px; left: 530px; width: 230px; text-align: center; font-size: 31px; line-height: 1.55; }

  .theme-initial { top: 212px; left: 272px; font-size: 300px; line-height: 1; color: var(--cyan); }
  .theme-rest { top: 318px; left: 396px; font-size: 76px; line-height: 1; color: var(--cyan); white-space: nowrap; }
  .verse { top: 404px; left: 490px; font-size: 32px; }

  .date-pill { top: 530px; left: 372px; width: 420px; height: 94px; background: var(--white);
    border-radius: 34px 0 0 34px; color: var(--cyan); display: flex; flex-direction: column;
    justify-content: center; padding-left: 30px; font-size: 35px; line-height: 1.2; letter-spacing: .5px; }

  .cost { top: 664px; left: 520px; font-size: 31px; }

  .team-band { top: 760px; left: 0; width: 100%; height: 66px; background: var(--band);
    display: flex; align-items: center; font-size: 24px; }
  .team-band .role { width: 348px; text-align: center; }
  .team-band .role + .role { flex: 1; }
  .team-band .divider { width: 4px; height: 44px; background: var(--white); }

  .churches { top: 870px; left: 0; width: 100%; text-align: center; font-size: 24px; line-height: 1.45; }
  .registration { top: 982px; left: 30px; font-family: "Tinos", serif; font-style: italic; font-weight: 700; font-size: 24px; line-height: 1.3; }
  .registration .mark { position: absolute; left: -18px; top: 2px; font-size: 34px; font-style: normal; }
  .registration p + p { padding-left: 14px; }

  .shirt { top: 1056px; width: 190px; height: 144px;
    background: linear-gradient(180deg, #6a9be0 0%, var(--shirt) 45%, var(--shirt-dark) 100%); }
  .shirt-left { left: 0; }
  .shirt-right { right: 0; }
  .shirt-band { top: 1146px; left: 190px; width: 396px; height: 54px; background: rgba(200,215,255,.55);
    display: flex; align-items: center; justify-content: center; font-size: 22px; }
</style>
</head>
<body>
<main class="flyer">
  <h1 class="abs headline script">Are you a <span class="accent">Youth</span> aged 11 to 18!</h1>
  <p class="abs invite script"><span class="accent">Come</span> <span class="plain">and</span> <span class="accent">Enjoy</span> <span class="plain">with us</span></p>

  <div class="abs photo photo-speaker" role="img" aria-label="Portrait photo of speaker Dr. Morton Pasley"></div>
  <div class="abs photo photo-worship" role="img" aria-label="Photo of worship leader Glen Abernathy performing"></div>

  <h2 class="abs event-name sans">Harvest Rally<br>2013</h2>

  <span class="abs theme-initial script">L</span>
  <span class="abs theme-rest script">ife by Faith</span>
  <p class="abs verse serif">Hebrews 11:1-39</p>

  <div class="abs date-pill sans">
    <span>6TH, 8TH - 10TH</span>
    <span>FEBRUARY 2013</span>
  </div>

  <p class="abs cost serif">Cost: $25</p>

  <div class="abs team-band serif">
    <span class="role">Speaker - Dr. Morton Pasley</span>
    <span class="divider"></span>
    <span class="role">Worship Leader - Glen Abernathy</span>
  </div>

  <div class="abs churches serif">
    <p>Churches:</p>
    <p>FBC Marrow Creek, Venhurst Methodist, FBC Venhurst,</p>
    <p>Orrin Baptist, Hal Prewitt Ridge C of C, &amp; Marrow Creek C of C</p>
  </div>

  <div class="abs registration">
    <span class="mark">*</span>
    <p>Registration forms can be picked up in the office</p>
    <p>or from one of the churches.</p>
  </div>

  <div class="abs shirt shirt-left" role="img" aria-label="Photo of the blue event t-shirt, front"></div>
  <div class="abs shirt shirt-right" role="img" aria-label="Photo of the blue event t-shirt with theme print"></div>
  <div class="abs shirt-band serif">T-shirt for the event</div>
</main>
</body>
</html>
```